New Zealand Luggage Importer Needs Business Cards

We need professional, creative and fashionable business cards created.
We are based in New Zealand and import and distribute high-end, quality, fashionable and durable luggage.
We pride ourselves on selling the very best quality luggage, second only to 1 brand (which we won't mention here)...we use the same manufacturer. However, our prices are much more reasonable.
Industry/Entity Type
Business
Contact Information for Business Card
Mark Dunsley
027 512 4068
3/17 Harlow Street, Pinecrest Flats, Auckland, 0614
PO Box 204377, Fernside, Auckland 0731
09-528-3916
sales@brivancases.co.nz / www.brivancases.co.nz

```html
<!DOCTYPE html>
<html lang="en">
<head>
<meta charset="utf-8">
<title>Brivan Cases – Business Card</title>
<link rel="stylesheet" href="https://fonts.googleapis.com/css2?family=Michroma&family=PT+Sans:wght@400&display=swap">
<style>
  :root {
    --backdrop-top: #c9c9c9;
    --backdrop-bottom: #a8a8a8;
    --card: #262525;
    --watermark: #2d2c2c;
    --gold-light: #e3c77a;
    --gold: #c9a453;
    --gold-dark: #9c7a34;
    --text-grey: #c4c4c4;
    --white: #ffffff;
    --icon-ink: #2a2622;
  }
  * { margin: 0; padding: 0; box-sizing: border-box; }
  html, body { width: 1200px; height: 900px; overflow: hidden; }
  body {
    position: relative;
    background: linear-gradient(180deg, var(--backdrop-top), var(--backdrop-bottom));
    font-family: "PT Sans", "Myriad Pro", sans-serif;
  }
  .card {
    position: absolute;
    top: 170px;
    width: 347px;
    height: 560px;
    background: var(--card);
    overflow: hidden;
    box-shadow: 0 1px 3px rgba(0,0,0,0.25);
  }
  .card--front { left: 259px; }
  .card--back { left: 631px; }

  .watermark {
    position: absolute;
    left: 50%;
    top: 50%;
    transform: translate(-50%, -50%) rotate(-61deg);
    font-family: "Michroma", sans-serif;
    font-size: 58px;
    white-space: nowrap;
    color: var(--watermark);
    letter-spacing: 2px;
    pointer-events: none;
  }

  .holder-name {
    position: absolute;
    top: 56px;
    width: 100%;
    text-align: center;
    font-family: "Michroma", sans-serif;
    font-size: 25px;
    letter-spacing: 0.5px;
    background: linear-gradient(180deg, var(--gold-light), var(--gold) 55%, var(--gold-dark));
    -webkit-background-clip: text;
    background-clip: text;
    color: transparent;
  }

  .contact-icon {
    position: absolute;
    left: 149px;
    width: 48px;
    height: 48px;
  }
  .contact-icon--phone { top: 127px; }
  .contact-icon--web { top: 249px; }
  .contact-icon--location { top: 370px; }

  .contact-lines {
    position: absolute;
    width: 100%;
    text-align: center;
    font-size: 15px;
    line-height: 20px;
    color: var(--text-grey);
  }
  .contact-lines--phone { top: 188px; }
  .contact-lines--web { top: 304px; }
  .contact-lines--street { top: 427px; }
  .contact-lines--postal { top: 478px; }

  .brand-name {
    position: absolute;
    top: 266px;
    width: 100%;
    text-align: center;
    font-family: "Michroma", sans-serif;
    font-size: 25px;
    letter-spacing: 1px;
    color: var(--white);
  }

  .back-web {
    position: absolute;
    top: 485px;
    width: 100%;
    text-align: center;
    font-family: "Michroma", sans-serif;
    font-size: 11.5px;
    letter-spacing: 1.2px;
    color: var(--white);
  }
  .back-web .back-web__domain { color: var(--gold); }
</style>
</head>
<body>

<svg width="0" height="0" style="position:absolute">
  <defs>
    <radialGradient id="goldDisc" cx="40%" cy="30%" r="75%">
      <stop offset="0%" stop-color="#f0d98f"/>
      <stop offset="55%" stop-color="#cfa94f"/>
      <stop offset="100%" stop-color="#9a7631"/>
    </radialGradient>
  </defs>
</svg>

<section class="card card--front" aria-label="Business card front">
  <div class="watermark" aria-hidden="true">BRIVAN CASES</div>

  <h1 class="holder-name">MARK DUNSLEY</h1>

  <svg class="contact-icon contact-icon--phone" viewBox="0 0 48 48" aria-hidden="true">
    <circle cx="24" cy="24" r="24" fill="url(#goldDisc)"/>
    <path d="M17.5 14.5c1-.6 2-.4 2.6.5l2 3.2c.5.9.3 1.9-.5 2.5l-1.3 1c.9 2.2 2.7 4.1 5 5.1l1-1.3c.6-.8 1.6-1 2.5-.5l3.2 2c.9.6 1.1 1.7.5 2.6l-1.1 1.7c-.8 1.2-2.3 1.7-3.7 1.2-5.4-1.9-9.6-6.1-11.4-11.5-.5-1.4 0-2.9 1.2-3.7z" fill="var(--icon-ink)"/>
  </svg>
  <p class="contact-lines contact-lines--phone">09-528-3916<br>027 512 4068</p>

  <svg class="contact-icon contact-icon--web" viewBox="0 0 48 48" aria-hidden="true">
    <circle cx="24" cy="24" r="24" fill="url(#goldDisc)"/>
    <circle cx="24" cy="24" r="10.5" fill="var(--icon-ink)"/>
    <path d="M17 19c1.5-.5 3 .3 3.5 1.5.4 1-.6 1.8-.2 2.8.5 1 1.8.8 2.2 1.8.3.9-.4 2-1.2 2.6-.2-1.5-1.6-2-2.4-3-.8-1-.6-2.4-1.9-3.1zM25 15.5c1.3.3 2 1.1 1.6 2-.4.7-1.6.4-1.9 1.2-.2.8.8 1.2 1.6 1.3 1 .1 1.8-.6 2.8-.2.9.4 1.1 1.6.7 2.5-.5 1.1-1.8 1.2-2.5 2.1-.7.9-.4 2.3-1.3 3.2-.5-1.2-1.7-1.9-1.8-3.2 0-1 .7-1.8.2-2.6-.6-.8-2-.6-2.6-1.4-.5-.8.1-1.9.8-2.5.7-.6 1.6-.9 2.4-2.4z" fill="url(#goldDisc)"/>
  </svg>
  <p class="contact-lines contact-lines--web">sales@brivancases.co.nz<br>www.brivancases.co.nz</p>

  <svg class="contact-icon contact-icon--location" viewBox="0 0 48 48" aria-hidden="true">
    <circle cx="24" cy="24" r="24" fill="url(#goldDisc)"/>
    <path d="M24 13c-4.4 0-7.8 3.4-7.8 7.7 0 5.6 7.8 14.3 7.8 14.3s7.8-8.7 7.8-14.3c0-4.3-3.4-7.7-7.8-7.7z" fill="var(--icon-ink)"/>
    <circle cx="24" cy="20.8" r="2.8" fill="url(#goldDisc)"/>
  </svg>
  <p class="contact-lines contact-lines--street">3/17 Harlow Street, Pinecrest<br>Flats, Auckland, 0614</p>
  <p class="contact-lines contact-lines--postal">PO Box 204377, Fernside,<br>Auckland 0731</p>
</section>

<section class="card card--back" aria-label="Business card back">
  <div class="watermark" aria-hidden="true">BRIVAN CASES</div>
  <h2 class="brand-name">BRIVAN CASES</h2>
  <p class="back-web">WWW.<span class="back-web__domain">BRIVANCASES</span>.CO.NZ</p>
</section>

</body>
</html>
```